flyer to promote aggregates company (special color aggregates)

We are existing one year and need more visibility.Therefor we are looking for a digital flyer, to be distributed to architects, study agencies, concrete and landscaping companies, etc.
Our job is to offer all special colored aggregates for the construction and landscaping industry to create new special worlds within an aesthetic aspect. Our speciality is to find quarries, logistics and organise the supply of different products within each project or supplier. More info on our website www.morvelstone.be (available in English).
The flyer should be class, modern and attractive. Idea is to invite to have a look on website and take on information with us. Imaging is central, a little text can be provided, in English, French and Dutch (we need these three languages, we can do the translations).
I have uploaded a previous home made brochure in English, which I used untill now to give around and promote our company... it is too much text. But gives other nice pictures. But I am not a specialist in that kind of things (made with MS Word).
Target Market(s)
architects, study engineering companies, precast concrete, concrete, landscaping and construction
Industry/Entity Type
Construction
Requirements
Must have
- - company logo
- - small part text
- - contact details !
- - pics

```html
<!DOCTYPE html>
<html lang="en">
<head>
<meta charset="utf-8">
<title>Morvelstone Aggregates – Flyer</title>
<link rel="stylesheet" href="https://fonts.googleapis.com/css2?family=Arimo:wght@400;700&family=Open+Sans:wght@400;600;700&display=swap">
<style>
  :root {
    --paper: #ffffff;
    --ink: #2b2b2b;
    --green: #9cc23a;
    --blue: #3a98d6;
    --steel: #7fa0cc;
    --olive: #6b6c3c;
    --rule: #c9c9c9;
  }
  * { box-sizing: border-box; margin: 0; padding: 0; }
  html, body { width: 776px; height: 1200px; overflow: hidden; background: var(--paper); }
  .flyer {
    position: relative; width: 776px; height: 1200px; background: var(--paper);
    font-family: "Open Sans", Arial, sans-serif; color: var(--ink);
  }
  .gallery { position: absolute; top: 0; left: 0; width: 776px; height: 600px; }
  .tile { position: absolute; width: 388px; height: 200px; }
  .tile--l { left: 0; }
  .tile--r { left: 389px; width: 387px; }
  .row-1 { top: 0; } .row-2 { top: 200px; } .row-3 { top: 400px; }
  .tile--ochre  { background: radial-gradient(circle at 50% 50%, #a9866a 0%, #b89a80 55%, #e9e2da 100%); }
  .tile--black  { background: radial-gradient(circle at 50% 45%, #2a2b2e 0%, #3d3f44 60%, #d9dadc 100%); }
  .tile--slate  { background: radial-gradient(circle at 50% 50%, #4a5566 0%, #6a7383 60%, #e6e8ec 100%); }
  .tile--pebble { background: radial-gradient(circle at 50% 50%, #9a8a7c 0%, #b8a898 55%, #ece8e4 100%); }
  .tile--gold   { background: radial-gradient(circle at 50% 50%, #a88a4e 0%, #c4a572 55%, #efe9dd 100%); }
  .tile--red    { background: radial-gradient(circle at 50% 50%, #a8442e 0%, #c0654c 60%, #f1e4df 100%); }

  .block { position: absolute; }
  .block h2 { font-family: "Arimo", Arial, sans-serif; font-weight: 700; font-size: 28px; line-height: 34px; }
  .block p { font-size: 15.5px; line-height: 23px; margin-top: 10px; }
  .about { left: 19px; top: 634px; width: 350px; }
  .about h2 { color: var(--green); }
  .materials { left: 19px; top: 844px; width: 350px; }
  .materials h2 { color: var(--blue); }
  .logistics { left: 402px; top: 639px; width: 360px; }
  .logistics h2 { color: var(--steel); }
  .cta { position: absolute; left: 402px; top: 884px; width: 360px; text-align: center; font-size: 15.5px; line-height: 23px; }
  .cta strong { font-weight: 700; }

  .footer-rule { position: absolute; left: 0; top: 1057px; width: 776px; border-top: 1px dashed var(--rule); }
  .footer-divider { position: absolute; left: 387px; top: 1060px; height: 112px; border-left: 1px dotted var(--rule); }

  .brand { position: absolute; left: 30px; top: 1090px; display: flex; align-items: center; gap: 14px; }
  .brand__mark { width: 52px; height: 52px; background: var(--olive); }
  .brand__name {
    font-family: "Arimo", Arial, sans-serif; font-weight: 700; color: var(--olive);
    font-size: 28px; line-height: 30px; letter-spacing: 0.5px; text-transform: uppercase;
  }

  .contact { position: absolute; left: 407px; top: 1072px; font-family: "Arimo", Arial, sans-serif; font-size: 14px; color: var(--ink); list-style: none; }
  .contact li { height: 25.5px; line-height: 20px; }
  .contact li:first-child { font-family: "Open Sans", Arial, sans-serif; }
  .contact .label { font-weight: 700; }
  .label--tel { color: var(--green); }
  .label--mail { color: var(--steel); }
  .label--site { color: var(--blue); }
</style>
</head>
<body>
<main class="flyer">
  <section class="gallery">
    <div class="tile tile--l row-1 tile--ochre" role="img" aria-label="Close-up of ochre and brown crushed gravel"></div>
    <div class="tile tile--r row-1 tile--black" role="img" aria-label="Close-up of glossy black crushed aggregate"></div>
    <div class="tile tile--l row-2 tile--slate" role="img" aria-label="Close-up of blue-grey crushed stone"></div>
    <div class="tile tile--r row-2 tile--pebble" role="img" aria-label="Close-up of mixed colour rounded pebbles"></div>
    <div class="tile tile--l row-3 tile--gold" role="img" aria-label="Close-up of golden yellow crushed stone"></div>
    <div class="tile tile--r row-3 tile--red" role="img" aria-label="Close-up of red crushed granite chippings"></div>
  </section>

  <section class="block about">
    <h2>Who are we?</h2>
    <p>Morvelstone Aggregates is a specialized trader of natural, synthetic and recycled aggregates throughout Europe. These sand and gravels are available for all applications of concrete, public works, road works and landscaping development.</p>
  </section>

  <section class="block materials">
    <h2>Materials</h2>
    <p>Morvelstone Aggregates is continuously looking for new sources that are less available or even unknown in our regions and countries. Along these materials, we also offer the more classic and better known materials on your simple request.</p>
  </section>

  <section class="block logistics">
    <h2>Logistics</h2>
    <p>In Belgium we are on an interesting logistic square and Ghent has his impressive bulk-axed port. This multimodal location is ideal for import and export of materials from and into Europe. A well-developed logistic network and reliable infrastructure makes us operate through Europe easily.</p>
  </section>

  <p class="cta"><strong>Contact us</strong> to ask for more information and discover what we can do for you.</p>

  <div class="footer-rule"></div>
  <div class="footer-divider"></div>

  <div class="brand">
    <span class="brand__mark"></span>
    <span class="brand__name">Morvelstone<br>Aggregates</span>
  </div>

  <ul class="contact">
    <li>Kerkweg 22 – B-9950 Lievegem – Belgium</li>
    <li><span class="label label--tel">Tel.:</span> +32 (0)470 318 206</li>
    <li><span class="label label--mail">Mail:</span> info@morvelstone.be</li>
    <li><span class="label label--site">Site:</span> www.morvelstone.be</li>
  </ul>
</main>
</body>
</html>
```